I would like to start a new webpage for a dating site in switzerland.
The dating site is not a escort service at all and should not transmit any type of sexual connotation.
The is more a compagnionship dating : male pay to meet ladies for some time in which they invite them for dinner, coktail, museum visit or walking or even skying. the meeting will take place in big cities in switzerland: geneva, zurich, bern, lausannes.

Industry/Entity Type

Dating

```html
<!DOCTYPE html>
<html lang="en">
<head>
<meta charset="utf-8">
<title>Datewell – Companionship Dating in Switzerland</title>
<link href="https://fonts.googleapis.com/css2?family=Josefin+Sans:wght@400;600;700&family=Open+Sans:ital,wght@0,400;0,600;1,400&display=swap" rel="stylesheet">
<style>
:root{
  --pink:#ff6f7d;
  --pink-dark:#e9505f;
  --pink-soft:#f7a1aa;
  --ink:#2f3035;
  --text:#55575d;
  --muted:#8a8c92;
  --bar:#4b4e56;
  --field:#2d2f36;
  --line:#e2e2e4;
  --card:#f1f1f2;
  --grey-band:#ececec;
  --accent-green:#b6e04a;
}
*{box-sizing:border-box;margin:0;padding:0}
html,body{width:674px;height:1200px;overflow:hidden;background:#fff}
body{position:relative;font-family:"Open Sans",Arial,sans-serif;color:var(--text)}
.abs{position:absolute}
.head{font-family:"Josefin Sans",Arial,sans-serif}

/* top bar */
.topbar{left:0;top:0;width:674px;height:29px;background:var(--bar);color:#fff;font-size:7px}
.topbar .connect{left:104px;top:10px;font-weight:600}
.social{top:9px;width:8px;height:8px;border-radius:50%;background:#8d9099}
.topbar .member{left:392px;top:10px}
.topbar .member b{color:var(--accent-green);font-weight:600}
.topbar .phone{left:491px;top:9px;font-size:8.5px;color:#d8d9dc}

/* hero */
.hero{left:0;top:29px;width:674px;height:382px;background:linear-gradient(100deg,#3b4a6b 0%,#7a6f86 35%,#c98a6e 55%,#6d5a63 75%,#b7a7a8 100%)}
.nav{left:104px;top:29px;width:466px;height:50px;background:var(--pink);box-shadow:0 4px 10px rgba(0,0,0,.25)}
.brand{left:10px;top:13px;font-family:"Josefin Sans",sans-serif;font-weight:700;font-size:18px;color:#fff}
.nav ul{list-style:none;position:absolute;top:22px;left:194px;display:flex;gap:14px}
.nav li{font-family:"Josefin Sans",sans-serif;font-weight:600;font-size:9px;color:#fff;letter-spacing:.2px}
.nav li:first-child{margin-right:6px}

.signup{left:111px;top:112px;width:179px;height:281px;background:rgba(30,32,40,.78)}
.fb{left:14px;top:14px;width:151px;height:21px;background:#3a5d9e;color:#fff;font-size:7.5px;font-weight:600}
.fb i{position:absolute;left:9px;top:6px;width:9px;height:9px;background:#fff;border-radius:1px}
.fb span{position:absolute;left:40px;top:5px}
.or{left:0;width:179px;top:40px;text-align:center;font-size:7px;color:#c9cad0}
.signup h2{left:14px;top:50px;font-family:"Josefin Sans",sans-serif;font-weight:700;font-size:17px;color:var(--pink)}
.signup h2 span{color:#8e9098;font-weight:400}
.field{left:14px;width:151px;height:21px;background:var(--field);border:1px solid #4a4c55;font-size:5.5px;color:#cfd0d5;padding:7px 0 0 9px}
.cta{background:var(--pink);color:#fff;font-family:"Josefin Sans",sans-serif;font-weight:600;text-align:center;box-shadow:0 2px 0 var(--pink-dark)}
.signup .cta{left:14px;top:215px;width:151px;height:21px;font-size:8.5px;padding-top:6px}
.terms{left:14px;top:247px;width:155px;font-size:6px;line-height:9.5px;color:#c1c2c8}
.dots{top:390px;width:8px;height:8px;border:1px solid #fff;border-radius:50%}

/* activities */
.section-title{font-family:"Josefin Sans",sans-serif;font-weight:400;color:var(--pink);letter-spacing:.5px}
.activities-title{left:0;width:674px;top:440px;text-align:center;font-size:15px}
.activity{top:473px;width:86px;height:69px}
.activity-label{top:549px;font-size:7px;color:var(--ink)}
.activities .cta{left:263px;top:574px;width:117px;height:21px;font-size:8.5px;padding-top:6px}

/* cities */
.cities{left:0;top:610px;width:674px;height:207px;background:radial-gradient(ellipse at 55% 45%,#fafafa 0%,var(--grey-band) 60%)}
.cities .brandname{left:114px;top:65px;font-family:"Josefin Sans",sans-serif;font-weight:700;font-size:21px;color:var(--pink)}
.cities h3{left:116px;top:97px;font-family:"Josefin Sans",sans-serif;font-weight:400;font-size:17px;color:var(--ink);letter-spacing:.5px}
.cities h3 span{color:var(--pink-soft)}
.cities .cta{left:122px;top:127px;width:118px;height:20px;font-size:8.5px;padding-top:5px}
.map{left:288px;top:14px;width:236px;height:144px;border-radius:30px 50px 40px 60px;background:radial-gradient(ellipse at center,#fff 0%,#f3dfe1 100%);border:1px solid #f4b7bd}
.map-shadow{left:320px;top:171px;width:190px;height:12px;border-radius:50%;background:radial-gradient(ellipse at center,rgba(0,0,0,.25),rgba(0,0,0,0) 70%)}

/* columns */
.col-title{top:835px;font-size:11.5px}
.col-rule{top:855px;width:142px;height:1px;background:var(--pink-soft)}
.thumb{width:64px;height:44px}
.meet-name{font-family:"Josefin Sans",sans-serif;font-size:8.5px;color:var(--pink)}
.meet-info{font-size:6px;line-height:9.5px;color:var(--ink)}
.comments{font-size:5.5px;color:var(--ink)}
.comments i{position:absolute;left:-13px;top:-1px;width:9px;height:7px;border:1.3px solid #555;border-radius:50%}
.view{width:41px;height:11px;background:var(--pink);color:#fff;font-size:5px;text-align:center;padding-top:2.5px}
.meet-rule{width:142px;height:1px;background:var(--line)}

.news{left:266px;width:142px;height:70px;background:var(--card)}
.news .date{left:0;top:0;width:24px;height:24px;background:var(--pink);color:#fff;font-size:5px;line-height:5.5px;text-align:center;padding-top:3px}
.news .lead{left:29px;top:6px;width:110px;font-size:6px;line-height:7.5px;font-weight:600;color:var(--ink)}
.news .body{left:5px;top:35px;width:132px;font-size:4.6px;line-height:7.8px;font-style:italic;color:var(--muted)}
.news .body b{color:var(--ink);font-style:normal}

.story-img{left:422px;width:141px;height:84px}
.story-title{left:422px;font-size:6px;color:var(--pink)}
.story-text{left:422px;width:141px;font-size:5.6px;line-height:8px;font-style:italic;color:var(--muted)}

/* footer */
.footer{left:0;top:1131px;width:674px;height:69px;background:var(--bar);color:#fff}
.footer .links{left:104px;top:22px;font-size:6.3px;word-spacing:1px}
.footer .links span{margin:0 5px;color:#aeb0b6}
.footer .copy{left:104px;top:38px;font-size:6.3px}
.footer .mail{left:330px;top:33px;width:9px;height:7px;background:var(--pink)}
.footer .newsletter{left:345px;top:32px;font-size:6.5px}
.footer .input{left:404px;top:30px;width:106px;height:14px;background:#3f4249;border:1px solid #5a5d65}
.footer .subscribe{left:509px;top:30px;width:52px;height:14px;background:var(--pink);font-size:5px;text-align:center;padding-top:4px}
</style>
</head>
<body>

<header class="abs topbar">
  <span class="abs connect">Connect With Us</span>
  <span class="abs social" style="left:164px"></span>
  <span class="abs social" style="left:179px"></span>
  <span class="abs social" style="left:195px"></span>
  <span class="abs social" style="left:210px"></span>
  <span class="abs member">Already a Member? <b>LOG IN</b></span>
  <span class="abs phone">
    <svg width="8" height="8" viewBox="0 0 8 8" style="vertical-align:-1px;margin-right:4px"><rect x="0" y="0" width="8" height="8" rx="1.5" fill="#c9cacf"/><path d="M2.2 1.8c.4 1.9 1.6 3.3 3.8 4.2l.5-1-1-.6-.5.5C4.2 4.5 3.6 3.9 3.3 3.1l.5-.5-.6-1z" fill="#4b4e56"/></svg>+1 (555) 014-2290
  </span>
</header>

<section class="abs hero" role="img" aria-label="Photo of a smiling couple embracing at a city fair at dusk"></section>

<nav class="abs nav">
  <span class="abs brand">Datewell</span>
  <ul>
    <li>HOME</li><li>ABOUT US</li><li>DATING TIPS</li><li>FAQ'S</li><li>CONTACT US</li>
  </ul>
</nav>

<form class="abs signup">
  <div class="abs fb"><i></i><span>Sign Up With Social Account</span></div>
  <div class="abs or">or</div>
  <h2 class="abs">Meet Your <span>Ladies</span></h2>
  <div class="abs field" style="top:76px">Me Looking For A Companion</div>
  <div class="abs field" style="top:102px">Name</div>
  <div class="abs field" style="top:128px">Age</div>
  <div class="abs field" style="top:156px">Place</div>
  <div class="abs field" style="top:182px">Date</div>
  <div class="abs cta">FIND YOUR LADIES</div>
  <p class="abs terms">By clicking "Find Your Ladies" you agree with the Terms and Conditions and Privacy Policy.</p>
</form>

<span class="abs dots" style="left:315px"></span>
<span class="abs dots" style="left:327px"></span>
<span class="abs dots" style="left:339px"></span>
<span class="abs dots" style="left:351px"></span>

<section class="activities">
  <h2 class="abs section-title activities-title">COMPAGNIONSHIP DATING</h2>
  <div class="abs activity" style="left:110px;background:linear-gradient(135deg,#3a2a25,#8a5a45)" role="img" aria-label="Couple at a dinner table"></div>
  <div class="abs activity" style="left:202px;background:linear-gradient(135deg,#c23a3a,#e99a9a)" role="img" aria-label="Red cocktails with mint"></div>
  <div class="abs activity" style="left:294px;background:linear-gradient(135deg,#c9c3b4,#8b8574)" role="img" aria-label="Couple visiting a museum gallery"></div>
  <div class="abs activity" style="left:386px;background:linear-gradient(135deg,#9fb56a,#5f7a3a)" role="img" aria-label="Couple walking in a park"></div>
  <div class="abs activity" style="left:477px;background:linear-gradient(135deg,#dfe3ea,#b33a3a)" role="img" aria-label="Couple skiing in the snow"></div>
  <span class="abs activity-label" style="left:110px">Dinner</span>
  <span class="abs activity-label" style="left:202px">Cocktail</span>
  <span class="abs activity-label" style="left:294px">Museum Visit</span>
  <span class="abs activity-label" style="left:386px">Walking</span>
  <span class="abs activity-label" style="left:477px">Skying</span>
  <div class="abs cta">SIGN UP NOW !</div>
</section>

<section class="abs cities">
  <span class="abs brandname">Datewell</span>
  <h3 class="abs">MEETING <span>CITIES</span></h3>
  <div class="abs cta">SEARCH LADIES NOW !</div>
  <div class="abs map" role="img" aria-label="Outline map of Switzerland marking Zurich and Geneva"></div>
  <div class="abs map-shadow"></div>
</section>

<!-- Recent meets -->
<h2 class="abs section-title col-title" style="left:110px">RECENT MEETS</h2>
<div class="abs col-rule" style="left:110px"></div>

<div class="abs thumb" style="left:110px;top:866px;background:linear-gradient(135deg,#c89a7a,#7aa04a)" role="img" aria-label="Portrait of a laughing couple"></div>
<span class="abs meet-name" style="left:182px;top:869px">Leon &amp; Clara</span>
<p class="abs meet-info" style="left:182px;top:881px">NEW<br>25, Female, 5'0/152 cm<br>Zurich ,Switzerland</p>
<span class="abs comments" style="left:124px;top:925px"><i></i>Comments</span>
<span class="abs view" style="left:207px;top:923px">VIEW DETAILS</span>
<div class="abs meet-rule" style="left:110px;top:940px"></div>

<div class="abs thumb" style="left:110px;top:952px;background:linear-gradient(135deg,#d9b49a,#8a6a55)" role="img" aria-label="Portrait of a smiling woman"></div>
<span class="abs meet-name" style="left:182px;top:954px">Leon &amp; Clara</span>
<p class="abs meet-info" style="left:182px;top:966px">NEW<br>25, Female, 5'0/152 cm<br>Zurich ,Switzerland</p>
<span class="abs comments" style="left:124px;top:1010px"><i></i>Comments</span>
<span class="abs view" style="left:207px;top:1008px">VIEW DETAILS</span>
<div class="abs meet-rule" style="left:110px;top:1025px"></div>

<div class="abs thumb" style="left:110px;top:1036px;background:linear-gradient(135deg,#e8e4e4,#c0303a)" role="img" aria-label="Couple in winter jackets"></div>
<span class="abs meet-name" style="left:182px;top:1039px">Leon &amp; Clara</span>
<p class="abs meet-info" style="left:182px;top:1051px">NEW<br>25, Female, 5'0/152 cm<br>Zurich ,Switzerland</p>
<span class="abs comments" style="left:124px;top:1095px"><i></i>Comments</span>
<span class="abs view" style="left:207px;top:1092px">VIEW DETAILS</span>
<div class="abs meet-rule" style="left:110px;top:1109px"></div>

<!-- News -->
<h2 class="abs section-title col-title" style="left:266px">NEWS</h2>
<div class="abs col-rule" style="left:266px"></div>

<article class="abs news" style="top:866px">
  <div class="abs date">24TH<br>DEC<br>2014</div>
  <p class="abs lead">Lorem Ipsum is simply dummy text of the printing and typesetting industry.</p>
  <p class="abs body">Lorem Ipsum has been the industry's standard dummy text ever since the 1500s, when an unknown printer took a galley of type and scrambled it to make a type specimen book<b>...Read More</b></p>
</article>
<article class="abs news" style="top:952px">
  <div class="abs date">24TH<br>DEC<br>2014</div>
  <p class="abs lead">Lorem Ipsum is simply dummy text of the printing and typesetting industry.</p>
  <p class="abs body">Lorem Ipsum has been the industry's standard dummy text ever since the 1500s, when an unknown printer took a galley of type and scrambled it to make a type specimen book<b>...Read More</b></p>
</article>
<article class="abs news" style="top:1038px">
  <div class="abs date">24TH<br>DEC<br>2014</div>
  <p class="abs lead">Lorem Ipsum is simply dummy text of the printing and typesetting industry.</p>
  <p class="abs body">Lorem Ipsum has been the industry's standard dummy text ever since the 1500s, when an unknown printer took a galley of type and scrambled it to make a type specimen book<b>...Read More</b></p>
</article>

<!-- Stories -->
<h2 class="abs section-title col-title" style="left:422px">MEET FOR DATE&nbsp; STORIES</h2>
<div class="abs col-rule" style="left:422px;width:141px"></div>

<div class="abs story-img" style="top:866px;background:linear-gradient(135deg,#e9e4df,#c7a08a)" role="img" aria-label="Happy couple smiling together"></div>
<span class="abs story-title" style="top:955px">Love story of Marc and Elise</span>
<p class="abs story-text" style="top:964px">Lorem Ipsum is simply dummy text of the printing and typesetting industry.</p>

<div class="abs story-img" style="top:996px;background:linear-gradient(135deg,#d8c6a8,#9c8a70)" role="img" aria-label="Couple reading a city map on holiday"></div>
<span class="abs story-title" style="top:1085px">Love story of Marc and Elise</span>
<p class="abs story-text" style="top:1096px">Lorem Ipsum is simply dummy text of the printing and typesetting industry.</p>

<footer class="abs footer">
  <p class="abs links">Home<span>|</span>About Us<span>|</span>Dating Tips<span>|</span>FAQ's<span>|</span>Contact us</p>
  <p class="abs copy">© 2014 Company Name, All Rights Reserved</p>
  <span class="abs mail"></span>
  <span class="abs newsletter">Newsletter SignUp</span>
  <span class="abs input"></span>
  <span class="abs subscribe">SUBSCRIBE</span>
</footer>

</body>
</html>
```